Door Knocker Design Front & Back

Front needs to be attention grabbing. Would like to highlight that we offer financing as well. Size of this needs to be 4" x 11".
Attached is our business cards front and back as well as our logo+

```html
<!DOCTYPE html>
<html lang="en">
<head>
<meta charset="utf-8">
<title>Northfield Homes – Door Hanger Front &amp; Back</title>
<link href="https://fonts.googleapis.com/css2?family=Bebas+Neue&family=Poppins:ital,wght@0,400;0,500;0,600;0,700;1,700;1,800&family=Audiowide&display=swap" rel="stylesheet">
<style>
  :root{
    --orange:#ee5a24;
    --ink:#161616;
    --black:#1a1a1a;
    --white:#ffffff;
    --page:#5e5e5e;
    --sky-top:#a9c4ea;
    --sky-mid:#eef2f8;
    --dusk:#f6c79a;
    --lawn:#5f8a3a;
  }
  html,body{margin:0;padding:0;}
  body{width:1200px;height:2617px;overflow:hidden;background:var(--page);position:relative;font-family:"Poppins",sans-serif;}
  .hanger{position:absolute;top:592px;width:540px;height:1433px;overflow:hidden;box-shadow:6px 8px 14px rgba(0,0,0,.45);}
  .hanger--front{left:40px;}
  .hanger--back{left:620px;}
  .sky{position:absolute;inset:0;}
  .hanger--front .sky{background:linear-gradient(180deg,var(--sky-top) 0%,var(--sky-mid) 35%,#f6ebe0 60%,var(--dusk) 78%,#f3d2b5 100%);}
  .hanger--back .sky{background:linear-gradient(180deg,var(--sky-top) 0%,var(--sky-mid) 30%,#f4f6fa 60%,#e9eef5 100%);}
  .photo{position:absolute;left:0;width:540px;}
  .hanger--front .photo{top:960px;height:400px;background:linear-gradient(180deg,rgba(246,199,154,0) 0%,#8c7a68 25%,#7c6a5a 55%,var(--lawn) 70%,#4f7a2e 100%);}
  .hanger--back .photo{top:865px;height:500px;background:linear-gradient(180deg,rgba(233,238,245,0) 0%,#9a8e86 15%,#7d716d 50%,#6d8a4a 72%,var(--lawn) 100%);}
  .art{position:absolute;left:0;top:0;}
  .brand{position:absolute;left:0;right:0;top:282px;text-align:center;font-family:"Poppins",sans-serif;font-weight:600;font-size:30px;color:var(--ink);letter-spacing:2px;}
  .headline{position:absolute;left:0;right:0;text-align:center;font-family:"Bebas Neue",sans-serif;line-height:1;margin:0;}
  .headline--top{top:368px;font-size:104px;color:var(--orange);transform:scaleY(1.05);}
  .headline--bottom{top:500px;font-size:110px;color:var(--ink);}
  .amp{position:absolute;left:251px;top:464px;width:36px;height:36px;border-radius:50%;background:var(--orange);color:var(--white);font-size:24px;line-height:36px;text-align:center;font-weight:500;}
  .promo{position:absolute;left:62px;top:612px;width:414px;height:129px;background:var(--orange);text-align:center;}
  .promo__lead{margin:12px 0 0;font-size:23px;line-height:24px;color:var(--white);font-weight:400;text-transform:uppercase;}
  .promo__punch{margin:2px 0 0;font-family:"Bebas Neue",sans-serif;font-size:60px;line-height:58px;color:var(--ink);}
  .contact{position:absolute;left:62px;}
  .contact__phone{display:flex;align-items:center;gap:14px;font-weight:700;font-size:54px;color:var(--ink);letter-spacing:1px;white-space:nowrap;}
  .hanger--front .contact__phone{top:768px;}
  .hanger--back .contact__phone{top:758px;left:46px;}
  .contact__line{display:flex;align-items:flex-start;gap:18px;font-size:22.5px;line-height:27px;color:var(--ink);}
  .contact__line--address{top:855px;left:74px;}
  .contact__line--email{top:919px;left:74px;}
  .icon{flex:none;}
  .services-title{position:absolute;left:46px;top:392px;font-family:"Audiowide",sans-serif;font-size:32px;color:var(--ink);margin:0;letter-spacing:1px;}
  .services-title span{color:var(--orange);}
  .services{position:absolute;left:46px;top:458px;width:450px;height:180px;}
  .service{position:absolute;display:flex;align-items:center;gap:10px;font-size:20px;font-weight:500;color:var(--ink);line-height:19px;white-space:nowrap;}
  .financing{position:absolute;left:46px;top:651px;width:450px;height:62px;background:var(--orange);color:var(--white);font-style:italic;font-weight:800;font-size:30px;line-height:62px;text-align:center;white-space:nowrap;box-shadow:0 10px 10px -4px rgba(0,0,0,.35);}
  .site{position:absolute;left:0;right:0;top:1382px;text-align:center;font-size:25px;font-weight:500;letter-spacing:4px;color:var(--white);white-space:nowrap;}
  .site b{color:var(--orange);font-weight:700;}
</style>
</head>
<body>

<article class="hanger hanger--front">
  <div class="sky" role="img" aria-label="Sunset sky photograph"></div>
  <div class="photo" role="img" aria-label="Photograph of a finished single-storey home with lawn"></div>
  <svg class="art" width="540" height="1433" viewBox="0 0 540 1433" aria-hidden="true">
    <rect x="0" y="137" width="190" height="11" fill="#000"/>
    <circle cx="269" cy="142" r="86" fill="#000"/>
    <polygon points="0,1330 269,1270 540,1335 540,1433 0,1433" fill="var(--orange)"/>
    <polygon points="0,1347 269,1296 540,1352 540,1433 0,1433" fill="var(--black)"/>
  </svg>
  <div class="brand">NORTHFIELD HOMES</div>
  <h1 class="headline headline--top">REMODELLING</h1>
  <div class="amp">&amp;</div>
  <h2 class="headline headline--bottom">RESTORATION</h2>
  <div class="promo">
    <p class="promo__lead">Thinking you need a more<br>host-friendly space?</p>
    <p class="promo__punch">WE GOT YOU COVERED</p>
  </div>
  <div class="contact contact__phone">
    <svg class="icon" width="44" height="44" viewBox="0 0 44 44"><circle cx="22" cy="22" r="21" fill="var(--orange)"/><path d="M15 12c2-1 3 0 4 2l1 3c0 1-1 2-2 3 1 3 3 5 6 6 1-1 2-2 3-2l3 1c2 1 3 2 2 4-1 2-3 3-6 2-6-2-10-6-12-12-1-3 0-6 1-7z" fill="#fff"/></svg>
    555-014-2286
  </div>
  <div class="contact contact__line contact__line--address">
    <svg class="icon" width="24" height="28" viewBox="0 0 24 28"><path d="M12 1a10 10 0 0 1 10 10c0 7-10 16-10 16S2 18 2 11A10 10 0 0 1 12 1z" fill="var(--orange)"/><circle cx="12" cy="11" r="4" fill="#fff"/></svg>
    <span>118 Birchwood Lane Suite 40,<br>Riverton, IA, United States, Iowa</span>
  </div>
  <div class="contact contact__line contact__line--email">
    <svg class="icon" width="26" height="26" viewBox="0 0 26 26"><circle cx="13" cy="13" r="13" fill="var(--orange)"/><rect x="6" y="8" width="14" height="10" fill="none" stroke="#fff" stroke-width="1.8"/><path d="M6 8l7 6 7-6" fill="none" stroke="#fff" stroke-width="1.8"/></svg>
    <span>hello@northfieldhomes.com</span>
  </div>
  <div class="site">www.<b>northfieldhomes</b>.com</div>
</article>

<article class="hanger hanger--back">
  <div class="sky" role="img" aria-label="Soft sky photograph"></div>
  <div class="photo" role="img" aria-label="Photograph of a rebuilt covered rear deck on a two-storey home"></div>
  <svg class="art" width="540" height="1433" viewBox="0 0 540 1433" aria-hidden="true">
    <circle cx="240" cy="133" r="86" fill="#000"/>
    <rect x="320" y="128" width="220" height="11" fill="#000"/>
    <polygon points="0,1330 253,1270 540,1335 540,1433 0,1433" fill="var(--orange)"/>
    <polygon points="0,1347 253,1296 540,1352 540,1433 0,1433" fill="var(--black)"/>
  </svg>
  <div class="brand">NORTHFIELD HOMES</div>
  <h2 class="services-title">OUR <span>SERVICES</span></h2>
  <div class="services">
    <svg class="art" width="450" height="180" viewBox="0 0 450 180" aria-hidden="true">
      <g stroke="#555" stroke-width="1.2" stroke-dasharray="3 2">
        <line x1="0" y1="44" x2="180" y2="44"/><line x1="0" y1="100" x2="180" y2="100"/>
        <line x1="234" y1="44" x2="415" y2="44"/><line x1="234" y1="100" x2="415" y2="100"/>
      </g>
      <line x1="200" y1="8" x2="200" y2="150" stroke="#bbb" stroke-width="1.5"/>
    </svg>
    <div class="service" style="left:0;top:0"><svg class="icon" width="34" height="34" viewBox="0 0 34 34"><polygon points="17,1 31,9 31,25 17,33 3,25 3,9" fill="var(--orange)"/><path d="M10 18l7-6 7 6v7H10z" fill="#fff"/></svg>Basements</div>
    <div class="service" style="left:0;top:56px"><svg class="icon" width="34" height="34" viewBox="0 0 34 34"><polygon points="17,1 31,9 31,25 17,33 3,25 3,9" fill="var(--orange)"/><path d="M11 11h12v4H11zM15 15h4v9h-4z" fill="#fff"/></svg>Additions</div>
    <div class="service" style="left:0;top:112px"><svg class="icon" width="34" height="34" viewBox="0 0 34 34"><polygon points="17,1 31,9 31,25 17,33 3,25 3,9" fill="var(--orange)"/><rect x="10" y="11" width="14" height="12" fill="#fff"/><rect x="12" y="15" width="10" height="2" fill="var(--orange)"/></svg>Kitchens/<br>bathrooms</div>
    <div class="service" style="left:234px;top:0"><svg class="icon" width="34" height="34" viewBox="0 0 34 34"><polygon points="17,1 31,9 31,25 17,33 3,25 3,9" fill="var(--orange)"/><path d="M10 10h3v14h-3zM15.5 10h3v14h-3zM21 10h3v14h-3z" fill="#fff"/></svg>Mold/ Asbestos</div>
    <div class="service" style="left:234px;top:56px"><svg class="icon" width="34" height="34" viewBox="0 0 34 34"><polygon points="17,1 31,9 31,25 17,33 3,25 3,9" fill="var(--orange)"/><path d="M8 19l9-9 9 9v5H8z" fill="#fff"/></svg>Roofing</div>
    <div class="service" style="left:234px;top:112px"><svg class="icon" width="34" height="34" viewBox="0 0 34 34"><polygon points="17,1 31,9 31,25 17,33 3,25 3,9" fill="var(--orange)"/><path d="M10 10h14v3H10zM10 15h14v3H10zM10 20h14v3H10z" fill="#fff"/></svg>Siding</div>
  </div>
  <div class="financing">WE ALSO OFFER FINANCING</div>
  <div class="contact contact__phone">
    <svg class="icon" width="44" height="44" viewBox="0 0 44 44"><circle cx="22" cy="22" r="21" fill="var(--orange)"/><path d="M15 12c2-1 3 0 4 2l1 3c0 1-1 2-2 3 1 3 3 5 6 6 1-1 2-2 3-2l3 1c2 1 3 2 2 4-1 2-3 3-6 2-6-2-10-6-12-12-1-3 0-6 1-7z" fill="#fff"/></svg>
    555-014-2286
  </div>
  <div class="site">www.<b>northfieldhomes</b>.com</div>
</article>

</body>
</html>
```